New Plumbing Company

We are looking for a smart and creative business card design for our new plumbing company. We are looking for creativity and originality in our business cards.

Industry/Entity Type

Plumbing

Contact Information for Business Card

Crestline Plumbing
Peter Halvane
Managing Director
Telephone Number : 0481529604
Email : service@crestlineplumbing.com.au
Website : www.crestlineplumbing.com.au
Lic. 508264K

Colors
0692cd
33a6d7
000000

Requirements
Must have
• I want the business card to be designed on a black background using the blue tones i have selected as seen in the company logo.

```html
<!DOCTYPE html>
<html lang="en">
<head>
<meta charset="utf-8">
<title>Crestline Plumbing – Business Card</title>
<link href="https://fonts.googleapis.com/css2?family=Open+Sans:wght@400;700&display=swap" rel="stylesheet">
<style>
  :root {
    --card-black: #000000;
    --brand-blue: #0692cd;
    --brand-blue-light: #33a6d7;
    --text-white: #ffffff;
    --page-bg: #ffffff;
  }
  * { margin: 0; padding: 0; box-sizing: border-box; }
  html, body {
    width: 1200px;
    height: 1000px;
    overflow: hidden;
    background: var(--page-bg);
    font-family: "Open Sans", Arial, sans-serif;
  }
  .canvas {
    position: relative;
    width: 1200px;
    height: 1000px;
  }
  .card {
    position: absolute;
    top: 381px;
    width: 422px;
    height: 237px;
    background: var(--card-black);
    color: var(--text-white);
  }
  .card--front { left: 146px; }
  .card--back { left: 601px; }

  .brand {
    position: absolute;
    display: flex;
    align-items: center;
    gap: 8px;
    font-weight: 400;
    color: var(--text-white);
    white-space: nowrap;
  }
  .brand__dot {
    flex: none;
    border: 3px solid var(--brand-blue);
    border-radius: 50%;
  }
  .card--front .brand {
    right: 36px;
    top: 24px;
    font-size: 19px;
  }
  .card--front .brand__dot { width: 38px; height: 38px; }

  .card--back .brand {
    left: 50%;
    top: 50%;
    transform: translate(-50%, -50%);
    flex-direction: column;
    gap: 14px;
    font-size: 20px;
  }
  .card--back .brand__dot { width: 100px; height: 100px; border-width: 4px; }

  .person {
    position: absolute;
    left: 33px;
    top: 118px;
  }
  .person__name {
    font-size: 13px;
    font-weight: 700;
    line-height: 16px;
  }
  .person__title {
    font-size: 8.5px;
    line-height: 12px;
  }
  .contact {
    position: absolute;
    left: 33px;
    top: 162px;
    list-style: none;
  }
  .contact__item {
    display: flex;
    align-items: center;
    height: 15px;
    font-size: 9px;
  }
  .contact__icon {
    width: 11px;
    height: 11px;
    margin-right: 8px;
    flex: none;
  }
</style>
</head>
<body>
<main class="canvas">
  <section class="card card--front" aria-label="Business card front">
    <div class="brand">
      <span class="brand__dot"></span>
      <span class="brand__name">Crestline Plumbing</span>
    </div>
    <div class="person">
      <p class="person__name">Peter Halvane</p>
      <p class="person__title">Managing Director</p>
    </div>
    <ul class="contact">
      <li class="contact__item">
        <svg class="contact__icon" viewBox="0 0 11 11" aria-hidden="true">
          <rect x="3" y="0.5" width="5" height="10" rx="1" fill="none" stroke="#0692cd" stroke-width="1"/>
          <rect x="4.5" y="8.3" width="2" height="1" fill="#0692cd"/>
        </svg>
        <span>0481529604</span>
      </li>
      <li class="contact__item">
        <svg class="contact__icon" viewBox="0 0 11 11" aria-hidden="true">
          <circle cx="5.5" cy="5.5" r="4.5" fill="none" stroke="#33a6d7" stroke-width="0.9"/>
          <ellipse cx="5.5" cy="5.5" rx="2" ry="4.5" fill="none" stroke="#33a6d7" stroke-width="0.8"/>
          <line x1="1" y1="5.5" x2="10" y2="5.5" stroke="#33a6d7" stroke-width="0.8"/>
        </svg>
        <span>www.crestlineplumbing.com.au</span>
      </li>
      <li class="contact__item">
        <svg class="contact__icon" viewBox="0 0 11 11" aria-hidden="true">
          <rect x="0" y="2" width="11" height="7" fill="#0692cd"/>
          <polyline points="0,2 5.5,6 11,2" fill="none" stroke="#000" stroke-width="0.8"/>
        </svg>
        <span>service@crestlineplumbing.com.au</span>
      </li>
    </ul>
  </section>

  <section class="card card--back" aria-label="Business card back">
    <div class="brand">
      <span class="brand__dot"></span>
      <span class="brand__name">Crestline Plumbing</span>
    </div>
  </section>
</main>
</body>
</html>
```